Local fast-growing company in the service sector

We are looking for a modern business card design, which should also appear on our letterheads

Target Market(s)

Private and industrial sectors

Contact Information for Business Card

Vorname Name
Lindkofer Str. 18
71468 Remsbach
Tel.: 07163-418259-0
Name@kovaltec-pbz.de

Colors
9d9d9d
919191
aaaaaa

Requirements
Must have
• The logo (file) in silver

```html
<!DOCTYPE html>
<html lang="de">
<head>
<meta charset="utf-8">
<title>PBZ Visitenkarte</title>
<link rel="stylesheet" href="https://fonts.googleapis.com/css2?family=Open+Sans:wght@400;600;700&display=swap">
<style>
  :root {
    --backdrop: #1b1a1a;
    --card: #121212;
    --silver: #aaaaaa;
    --silver-mid: #9d9d9d;
    --silver-dim: #919191;
    --muted: #6e6e6e;
  }
  * { margin: 0; padding: 0; box-sizing: border-box; }
  html, body { width: 1200px; height: 1137px; overflow: hidden; background: var(--backdrop); }
  body { position: relative; font-family: "Open Sans", Arial, sans-serif; color: var(--silver); }

  .card {
    position: absolute;
    width: 680px; height: 430px;
    background: var(--card);
    box-shadow: 0 18px 40px rgba(0,0,0,.55);
  }
  .card--front { left: 70px; top: 80px; }
  .card--back { left: 450px; top: 620px; }

  .brand {
    position: absolute; right: 56px; top: 52px;
    display: flex; align-items: center; gap: 18px;
  }
  .brand__mark { width: 74px; height: 74px; border: 6px solid var(--silver); }
  .brand__text { display: flex; flex-direction: column; }
  .brand__name { font-size: 78px; font-weight: 700; line-height: .9; letter-spacing: 2px; color: var(--silver); }
  .brand__domain { font-size: 22px; font-weight: 400; color: var(--silver); letter-spacing: 1px; margin-top: 4px; }

  .person {
    position: absolute; left: 42px; top: 150px;
    border-left: 6px solid var(--silver-mid);
    padding-left: 10px;
  }
  .person__name { font-size: 21px; line-height: 1.15; color: var(--silver); }
  .person__title { font-size: 14px; color: var(--muted); }

  .contact {
    position: absolute; left: 60px; bottom: 44px;
    list-style: none; font-size: 19px; color: var(--silver-mid);
  }
  .contact li { display: flex; align-items: flex-start; gap: 14px; margin-top: 10px; line-height: 1.2; }
  .contact svg { width: 18px; height: 18px; flex: none; margin-top: 3px; fill: var(--silver-dim); }
  .contact .web { padding-left: 32px; margin-top: 22px; color: var(--silver-dim); }
</style>
</head>
<body>

<section class="card card--front">
  <div class="brand">
    <span class="brand__mark"></span>
    <div class="brand__text">
      <span class="brand__name">PBZ</span>
      <span class="brand__domain">kovaltec-pbz.de</span>
    </div>
  </div>

  <div class="person">
    <p class="person__name">Vorname Name</p>
    <p class="person__title">Job Title</p>
  </div>

  <ul class="contact">
    <li><svg viewBox="0 0 24 24"><path d="M12 2a7 7 0 0 0-7 7c0 5 7 13 7 13s7-8 7-13a7 7 0 0 0-7-7zm0 9.5A2.5 2.5 0 1 1 12 6.5a2.5 2.5 0 0 1 0 5z"/></svg><span>Lindkofer Str. 18<br>&nbsp;71468 Remsbach</span></li>
    <li><svg viewBox="0 0 24 24"><path d="M3 6c3-3 15-3 18 0l-1 3-4-1V6H8v2L4 9zM5 11h14v9H5zm4 2v2h2v-2zm4 0v2h2v-2zm-4 3v2h2v-2zm4 0v2h2v-2z"/></svg><span>07163-418259-0</span></li>
    <li><svg viewBox="0 0 24 24"><path d="M2 5h20v14H2zm2 2v.5l8 5.5 8-5.5V7zm0 3v7h16v-7l-8 5.5z"/></svg><span>Name@kovaltec-pbz.de</span></li>
    <li class="web">www.yourwebsite.com</li>
  </ul>
</section>

<section class="card card--back">
  <div class="brand">
    <span class="brand__mark"></span>
    <div class="brand__text">
      <span class="brand__name">PBZ</span>
      <span class="brand__domain">kovaltec-pbz.de</span>
    </div>
  </div>

  <ul class="contact">
    <li><svg viewBox="0 0 24 24"><path d="M12 2a7 7 0 0 0-7 7c0 5 7 13 7 13s7-8 7-13a7 7 0 0 0-7-7zm0 9.5A2.5 2.5 0 1 1 12 6.5a2.5 2.5 0 0 1 0 5z"/></svg><span>Lindkofer Str. 18<br>&nbsp;71468 Remsbach</span></li>
    <li><svg viewBox="0 0 24 24"><path d="M3 6c3-3 15-3 18 0l-1 3-4-1V6H8v2L4 9zM5 11h14v9H5zm4 2v2h2v-2zm4 0v2h2v-2zm-4 3v2h2v-2zm4 0v2h2v-2z"/></svg><span>07163-418259-0</span></li>
    <li><svg viewBox="0 0 24 24"><path d="M2 5h20v14H2zm2 2v.5l8 5.5 8-5.5V7zm0 3v7h16v-7l-8 5.5z"/></svg><span>Name@kovaltec-pbz.de</span></li>
    <li class="web">www.yourwebsite.com</li>
  </ul>
</section>

</body>
</html>
```